Mailer Design - Packaging for Candy Company

I need packaging design for a mailer. This is for a candy company.

I've attached the box image and template, current size is 9x6x3. There may be a small change but at this point this is the correct size.

This should be a gift worthy package, fun, colorful, clean, professional, and will be photographed and used as a primary selling point.

Industry/Entity Type

It Company

Colors
00a990
a9d046
fbed22
f78f20
f37122
ec1f27
e34197
0455a3
6b449b

Requirements
Must have
• Packaging should incorporate:
• Mira Bev's Candy
• Seattle, WA
• www.MiraBevsCandy.example
Nice to have
• I've attached three files with aspects that I like.
• Image 1- I like the different styles on the sides and top of the box. I like the multi-width stripes
• Image 2- I like the stripes
• Image 3- I like the badge style
• While these are aspects I like I am willing to take suggestions. I want to portray a bright, fun, candy company with a gift quality box.

```html
<!DOCTYPE html>
<html lang="en">
<head>
<meta charset="utf-8">
<title>Mira Bev's Candy – Mailer Box</title>
<link href="https://fonts.googleapis.com/css2?family=Rubik:wght@500;800&display=swap" rel="stylesheet">
<style>
  :root {
    --teal: #00a990;
    --lime: #a9d046;
    --yellow: #fbed22;
    --amber: #f78f20;
    --orange: #f37122;
    --red: #ec1f27;
    --pink: #e34197;
    --blue: #0455a3;
    --purple: #6b449b;
    --purple-soft: #7a5aa8;
    --magenta: #c8246b;
    --pill: #ecebf2;
    --white: #ffffff;
    --backdrop: #e4e4e6;
    --stripe-set:
      var(--purple) 0 16px, var(--white) 16px 32px,
      var(--blue) 32px 48px, var(--white) 48px 64px,
      var(--pink) 64px 80px, var(--white) 80px 96px,
      var(--red) 96px 112px, var(--white) 112px 128px,
      var(--orange) 128px 144px, var(--white) 144px 160px,
      var(--amber) 160px 176px, var(--white) 176px 192px,
      var(--yellow) 192px 208px, var(--white) 208px 224px,
      var(--lime) 224px 240px, var(--white) 240px 256px,
      var(--teal) 256px 272px, var(--white) 272px 288px;
  }
  * { box-sizing: border-box; margin: 0; padding: 0; }
  html, body { width: 1200px; height: 800px; overflow: hidden; }
  body {
    background: var(--backdrop);
    font-family: "Rubik", sans-serif;
    position: relative;
  }
  .brand-name {
    position: absolute;
    top: 30px;
    right: 40px;
    text-align: right;
    color: var(--purple);
    font-weight: 800;
    font-size: 48px;
    line-height: 1;
    text-transform: uppercase;
  }
  .mailer {
    position: absolute;
    left: 100px;
    top: 150px;
    display: grid;
    grid-template-columns: 600px 200px;
    grid-template-rows: 400px 200px;
  }
  .mailer-lid {
    position: relative;
    background: repeating-linear-gradient(120deg, var(--stripe-set));
  }
  .mailer-side {
    background: repeating-linear-gradient(90deg, var(--stripe-set));
    border-top: 2px solid rgba(0,0,0,0.08);
  }
  .lid-badge {
    position: absolute;
    left: 60px;
    top: 50px;
    width: 480px;
    height: 300px;
  }
  .badge-text {
    fill: var(--white);
    font-family: "Rubik", sans-serif;
    font-weight: 500;
    letter-spacing: 3px;
  }
  .badge-name {
    fill: var(--purple);
    font-family: "Rubik", sans-serif;
    font-weight: 800;
    font-size: 50px;
    text-transform: uppercase;
  }
  .mailer-end {
    position: relative;
    background: var(--magenta);
    border-left: 10px solid var(--teal);
    display: flex;
    align-items: flex-end;
    justify-content: center;
    padding-bottom: 24px;
  }
  .end-web {
    writing-mode: vertical-rl;
    transform: rotate(180deg);
    white-space: nowrap;
    color: var(--white);
    font-size: 13px;
    font-weight: 500;
  }
</style>
</head>
<body>
  <div class="brand-name">Mira Bev's<br>Candy</div>

  <div class="mailer">
    <div class="mailer-lid">
      <svg class="lid-badge" viewBox="0 0 620 380" xmlns="http://www.w3.org/2000/svg">
        <defs>
          <path id="badge-frame" d="M56 20 H564 A36 36 0 0 0 600 56 V324 A36 36 0 0 0 564 360 H56 A36 36 0 0 0 20 324 V56 A36 36 0 0 0 56 20 Z"/>
          <path id="tagline-arc" d="M150 100 Q310 40 470 100"/>
          <path id="city-arc" d="M200 300 Q310 345 420 300"/>
        </defs>
        <use href="#badge-frame" fill="none" stroke="var(--purple)" stroke-width="34"/>
        <use href="#badge-frame" fill="none" stroke="var(--yellow)" stroke-width="28"/>
        <use href="#badge-frame" fill="none" stroke="var(--teal)" stroke-width="16"/>
        <use href="#badge-frame" fill="none" stroke="var(--yellow)" stroke-width="6"/>
        <use href="#badge-frame" fill="var(--purple-soft)" stroke="var(--purple)" stroke-width="2"/>

        <circle cx="58" cy="190" r="6" fill="var(--white)"/>
        <circle cx="562" cy="190" r="6" fill="var(--white)"/>
        <circle cx="80" cy="60" r="5" fill="var(--white)"/>
        <circle cx="540" cy="320" r="5" fill="var(--white)"/>

        <rect class="badge-pill" x="90" y="115" width="440" height="150" rx="75" fill="var(--pill)" role="img" aria-label="Light candy pattern of lollipops, candy canes and wrapped sweets"/>

        <text class="badge-text" font-size="20">
          <textPath href="#tagline-arc" startOffset="50%" text-anchor="middle">Tagline of the company</textPath>
        </text>

        <text class="badge-name" x="310" y="182" text-anchor="middle">Mira Bev's</text>
        <text class="badge-name" x="310" y="236" text-anchor="middle">Candy</text>

        <text class="badge-text" font-size="24">
          <textPath href="#city-arc" startOffset="50%" text-anchor="middle">Seattle, WA</textPath>
        </text>
      </svg>
    </div>
    <div class="mailer-end">
      <span class="end-web">www.MiraBevsCandy.example</span>
    </div>
    <div class="mailer-side"></div>
  </div>
</body>
</html>
```